Velmira Body Oil Label for 4 -8 oz bottles

We are selling 4 and 8 oz body oils and need a label to put on our bottles. I'm not sure if we want a label for the front and also the back of the bottle or just one label in the front. You can give me examples of each way. Attached is our logo on a blue background but the background will change colors depending on the scent as specified in the design description. Our bottle will be either clear or white with a pump spray type lid as shown in the attached example. Attached are also our design criteria which is needed for the labels.
Updates

We have decided to use the disc top cap and not the pump spray cap. If you are able to, please show us the design on the 4 oz bottle with the disc top cap. Thanks

Target Market(s)

women

Industry/Entity Type

skincare, cosmetics

Font styles to use
Serif
Sans Serif

Requirements
Must have
• stylish name for each scented oil which contrasts the font in the logo. Also must have darker colors since the logo colors are lighter.
Nice to have
• Border around the labels, maybe one solid color or maybe two complimenting colors which go well with the fragrnace name
Should not have
• background colors that match the logo colors

```html
<!DOCTYPE html>
<html lang="en">
<head>
<meta charset="utf-8">
<title>Velmira Cotton Candy Body Oil Label</title>
<link rel="stylesheet" href="https://fonts.googleapis.com/css2?family=Inter+Tight:wght@300;400;600;800;900&display=swap">
<style>
  :root {
    --page: #ffffff;
    --label-pink: #ec8fbd;
    --label-pink-light: #f2a9cc;
    --ink-white: #ffffff;
    --ink-soft: #fde9f3;
  }
  * { margin: 0; padding: 0; box-sizing: border-box; }
  html, body {
    width: 800px;
    height: 1200px;
    overflow: hidden;
    background: var(--page);
  }
  body {
    display: flex;
    align-items: center;
    justify-content: center;
    font-family: "Inter Tight", Arial, sans-serif;
    color: var(--ink-white);
  }
  .label {
    width: 460px;
    height: 1160px;
    background: linear-gradient(180deg, var(--label-pink-light) 0%, var(--label-pink) 55%, var(--label-pink-light) 100%);
    display: flex;
    flex-direction: column;
    align-items: center;
    padding: 70px 26px 34px;
  }
  .brand {
    display: flex;
    flex-direction: column;
    align-items: center;
    margin-bottom: 40px;
  }
  .brand-row {
    display: flex;
    align-items: center;
    gap: 14px;
  }
  .brand-dot {
    width: 22px;
    height: 22px;
    border-radius: 50%;
    background: var(--ink-white);
  }
  .brand-name {
    font-weight: 300;
    font-size: 76px;
    letter-spacing: 1px;
    line-height: 1;
  }
  .brand-tag {
    align-self: flex-end;
    font-weight: 300;
    font-size: 24px;
    letter-spacing: 3px;
    margin-top: 8px;
  }
  .scent-name {
    font-weight: 900;
    font-size: 124px;
    line-height: 0.9;
    letter-spacing: -5px;
    text-align: center;
  }
  .product-type {
    font-weight: 400;
    font-size: 56px;
    margin-top: 6px;
    margin-bottom: 36px;
  }
  .claims {
    list-style: none;
    text-align: center;
    font-weight: 600;
    font-size: 21px;
    letter-spacing: 4px;
    line-height: 1.95;
    margin-bottom: 34px;
  }
  .fine-print {
    width: 100%;
    font-size: 15px;
    line-height: 1.45;
    color: var(--ink-soft);
  }
  .fine-print p { margin-bottom: 16px; }
  .fine-print strong { font-weight: 600; }
  .caps { text-transform: uppercase; }
  .footer {
    width: 100%;
    margin-top: auto;
    display: flex;
    justify-content: space-between;
    align-items: flex-end;
    font-size: 14px;
    color: var(--ink-soft);
  }
  .net {
    font-weight: 600;
    letter-spacing: 1px;
  }
</style>
</head>
<body>
  <main class="label">
    <header class="brand">
      <div class="brand-row">
        <span class="brand-dot"></span>
        <span class="brand-name">Velmira</span>
      </div>
      <span class="brand-tag">BODY OILS</span>
    </header>

    <h1 class="scent-name">Cotton<br>Candy</h1>
    <p class="product-type">Body Oil</p>

    <ul class="claims">
      <li>NON-GREASY</li>
      <li>WITH VITAMIN E</li>
      <li>ULTRA MOISTURIZING</li>
    </ul>

    <section class="fine-print">
      <p><strong>INGREDIENTS:</strong> Cocos Nucifera (Coconut) Oil, Prunus Amygdalus Dulcis (Almond) Oil, Vitis Vinifera (Grape) Seed Oil, Helianthus Annuus Seed Oil, Simmondsia Chinensis Oil, Tocopheryl Acetate, Fragrance.</p>
      <p><strong>DIRECTIONS:</strong> Apply a small amount to skin and massage until absorbed. Use daily for best results.</p>
      <p><strong>WARNINGS:</strong> For external use only.<br>
        <span class="caps">Avoid contact with eyes – discontinue use if irritation occurs. – Keep out of reach of children.</span> – Contains nut oils – use with caution if you have nut allergies.</p>
    </section>

    <footer class="footer">
      <span>Distributed by Velmira<br>Somerset, NJ 08873</span>
      <span class="net">NET 4 FL OZ</span>
    </footer>
  </main>
</body>
</html>
```